Brand New Church Business Card Design. Needs to appeal to high school students, professionals.

Business Card. Bold lines and colors. Simple font. This is a new church looking to attract new families who have moved to the area. Business professionals mostly. have a working logo. may need a little tweaking. Church is designed to do excellent ministries for students and children. Like business card design in box on mark vault homepage. Want a front and back side. Prefer colors to match the logo. But will lean on designers preferences and wisdom. DO NOT WANT A CROSS OR RELIGIOUS SYMBOL on the card.

Target Market(s)

Families, Professionals, Students

Industry/Entity Type

High School

Contact Information for Business Card

SaltRock ChurchSaltRock.atForrest Coulter904-515-8349Forrest@PineHollow.at

Font styles to use
Sans Serif

Colors
0255a3
ffffff

Requirements
Must have
• Bold colors. Very Masculine. Creative
Nice to have
• On printnook.markvault.com homepage in the business card design box. the card with the black, blue and gray looks really sharp. matches our logos.
Should not have
• no crosses or religious symbols.

```html
<!DOCTYPE html>
<html lang="en">
<head>
<meta charset="utf-8">
<title>PineHollow Church – Business Card</title>
<link href="https://fonts.googleapis.com/css2?family=Arimo:wght@400;700&display=swap" rel="stylesheet">
<style>
  :root {
    --stage: #2b2b2b;
    --brand-blue: #0255a3;
    --band-blue: #1a5590;
    --soft-blue: #4f8fd0;
    --ink: #050505;
    --paper: #ffffff;
    --mist: #d9d9d9;
    --name-blue: #2a6cb4;
  }
  * { margin: 0; padding: 0; box-sizing: border-box; }
  html, body {
    width: 1200px; height: 871px; overflow: hidden;
    background: var(--stage);
    font-family: "Arimo", Arial, sans-serif;
  }
  .stage { position: relative; width: 1200px; height: 871px; }
  .card {
    position: absolute; left: 280px; width: 640px; height: 366px;
    overflow: hidden; box-shadow: 0 10px 30px rgba(0,0,0,.5);
  }
  .card--back { top: 50px; background: var(--mist); }
  .card--front { top: 455px; background: var(--ink); }

  /* back side */
  .back-band { position: absolute; top: 0; height: 100%; background: var(--band-blue); }
  .back-band--left { left: 0; width: 160px; }
  .back-band--right { right: 0; width: 170px; }
  .back-field {
    position: absolute; left: 160px; width: 310px; top: 0; height: 100%;
    background: linear-gradient(180deg, #f2f2f2, #bdbdbd);
  }
  .back-plate {
    position: absolute; left: 160px; width: 310px; top: 100px; height: 170px;
    background: var(--ink);
    display: flex; align-items: center; justify-content: center;
  }

  /* brand lockup */
  .lockup { display: flex; align-items: center; gap: 12px; }
  .lockup__dot { width: 46px; height: 46px; border-radius: 50%; background: var(--soft-blue); flex: none; }
  .lockup__name {
    color: var(--paper); font-weight: 700; font-size: 26px; line-height: 1.05;
  }
  .lockup__name span { display: block; font-size: 20px; padding-left: 40px; }

  /* front side */
  .front-curve { position: absolute; inset: 0; }
  .contact { position: absolute; left: 40px; top: 145px; }
  .contact__name {
    color: var(--name-blue); font-weight: 700; font-size: 19px;
    letter-spacing: 4px; margin-bottom: 10px;
  }
  .contact__row {
    display: flex; align-items: center; gap: 6px;
    width: 250px; height: 24px; margin-bottom: 6px;
    background: var(--name-blue); color: var(--paper);
    font-size: 16px;
  }
  .contact__icon {
    width: 22px; height: 22px; margin-left: 2px; flex: none;
    background: var(--paper); display: flex; align-items: center; justify-content: center;
  }
  .front-logo { position: absolute; left: 345px; top: 140px; }
</style>
</head>
<body>
<main class="stage">

  <section class="card card--back" aria-label="Card back">
    <div class="back-band back-band--left"></div>
    <div class="back-field"></div>
    <div class="back-band back-band--right"></div>
    <div class="back-plate">
      <div class="lockup">
        <div class="lockup__dot"></div>
        <div class="lockup__name">PineHollow<span>Church</span></div>
      </div>
    </div>
  </section>

  <section class="card card--front" aria-label="Card front">
    <svg class="front-curve" width="640" height="366" viewBox="0 0 640 366">
      <path d="M0 0 H224 C300 90 305 250 270 366 H0 Z" fill="#ffffff"/>
    </svg>

    <div class="contact">
      <p class="contact__name">PELLISH</p>
      <div class="contact__row">
        <span class="contact__icon">
          <svg width="16" height="14" viewBox="0 0 16 14">
            <path d="M1 4 Q8 -1 15 4 L13 6 L11 4 H5 L3 6 Z" fill="#2a6cb4"/>
            <rect x="3" y="7" width="10" height="6" rx="1" fill="#2a6cb4"/>
          </svg>
        </span>
        904-555-0172
      </div>
      <div class="contact__row">
        <span class="contact__icon">
          <svg width="16" height="12" viewBox="0 0 16 12">
            <rect x="1" y="1" width="14" height="10" fill="none" stroke="#2a6cb4" stroke-width="1.6"/>
            <path d="M1 1 L8 7 L15 1" fill="none" stroke="#2a6cb4" stroke-width="1.6"/>
          </svg>
        </span>
        Dwayne@PineHollow.at
      </div>
    </div>

    <div class="front-logo lockup">
      <div class="lockup__dot"></div>
      <div class="lockup__name">PineHollow<span>Church</span></div>
    </div>
  </section>

</main>
</body>
</html>
```